Business Card Design

I need a business card for my rental business. The business is named:
Hire a Vorlatrike Brenmoor
www.hireavorlatrikebrenmoor.example
(555) 014-2937
This will be a business card that I will leave at other businesses as advertisement so it needs to have the name, website, and phone number.
Please feel free to be creative. This is a new business so I have no designs.
Thank you very much for your time and I look forward to receiving your designs
Target Market(s)
Local rental customers
Industry/Entity Type
Business
Contact Information for Business Card
Please check out my website:
Other font styles liked:
- anything creative
Colors
Designer to choose colors to be used in the design.
Requirements
Must have
- Business name, phone, website. Rentals available hourly or daily. Book online

```html
<!DOCTYPE html>
<html lang="en">
<head>
<meta charset="utf-8">
<title>Hire a Vorlatrike Brenmoor – Business Card</title>
<link href="https://fonts.googleapis.com/css2?family=Tinos:wght@700&family=Raleway:wght@300;500&display=swap" rel="stylesheet">
<style>
  :root {
    --page-bg: #e4e4e6;
    --sky-top: #2e2a66;
    --sky-mid: #4b3f86;
    --city-glow: #6a4e8e;
    --street-dark: #1d2240;
    --street-light: #6f8fbf;
    --vehicle-red: #8c2a3c;
    --ink-light: #f4f4f8;
    --panel-tint: rgba(255, 255, 255, 0.14);
  }
  * { margin: 0; padding: 0; box-sizing: border-box; }
  html, body {
    width: 1200px;
    height: 900px;
    overflow: hidden;
    background: var(--page-bg);
  }
  .business-card {
    position: absolute;
    left: 100px;
    top: 162px;
    width: 1000px;
    height: 576px;
    overflow: hidden;
    box-shadow: 0 10px 24px rgba(0, 0, 0, 0.18);
  }
  .card-scene {
    position: absolute;
    inset: 0;
    background:
      radial-gradient(ellipse 38% 30% at 32% 70%, var(--vehicle-red) 0%, rgba(140, 42, 60, 0) 100%),
      radial-gradient(ellipse 60% 40% at 60% 30%, var(--city-glow) 0%, rgba(106, 78, 142, 0) 100%),
      linear-gradient(180deg, var(--sky-top) 0%, var(--sky-mid) 38%, var(--street-dark) 66%, var(--street-light) 100%);
  }
  .brand-name {
    position: absolute;
    left: 185px;
    top: 100px;
    font-family: "Tinos", "Times New Roman", serif;
    font-weight: 700;
    font-size: 68px;
    line-height: 1.08;
    color: var(--ink-light);
  }
  .rental-note {
    position: absolute;
    left: 188px;
    top: 262px;
    font-family: "Raleway", "Helvetica Neue", Arial, sans-serif;
    font-weight: 500;
    font-size: 24px;
    line-height: 1.25;
    color: var(--ink-light);
    white-space: nowrap;
  }
  .contact-panel {
    position: absolute;
    left: 410px;
    top: 338px;
    width: 552px;
    height: 192px;
    background: var(--panel-tint);
  }
  .contact-row {
    position: absolute;
    left: 0;
    display: flex;
    align-items: flex-start;
  }
  .contact-row svg {
    flex: none;
    margin-left: 12px;
    fill: none;
    stroke: var(--ink-light);
  }
  .contact-text {
    position: absolute;
    left: 72px;
    font-family: "Raleway", "Helvetica Neue", Arial, sans-serif;
    font-weight: 300;
    font-size: 25px;
    line-height: 1.25;
    color: var(--ink-light);
    white-space: nowrap;
  }
  .row-address { top: 14px; }
  .row-web { top: 88px; }
  .row-phone { top: 142px; }
</style>
</head>
<body>
  <section class="business-card">
    <div class="card-scene" role="img" aria-label="Night photograph of a lit city skyline with a red three-wheeled roadster parked on a rooftop road"></div>

    <h1 class="brand-name">Hire a Vorlatrike<br>Brenmoor</h1>
    <p class="rental-note">Rentals available hourly or daily. Book online</p>

    <div class="contact-panel">
      <div class="contact-row row-address">
        <svg width="44" height="48" viewBox="0 0 44 48" aria-hidden="true">
          <path d="M22 44 C14 32 10 25 10 18 A12 12 0 0 1 34 18 C34 25 30 32 22 44 Z" fill="var(--ink-light)" stroke="none"/>
          <circle cx="22" cy="18" r="5" fill="#4b4a7a" stroke="none"/>
        </svg>
        <p class="contact-text" style="top:0">Route 88, Brenmoor, Westland 00417,<br>Norvania</p>
      </div>

      <div class="contact-row row-web">
        <svg width="44" height="44" viewBox="0 0 44 44" aria-hidden="true" stroke-width="2.4">
          <circle cx="22" cy="22" r="19"/>
          <ellipse cx="22" cy="22" rx="8" ry="19"/>
          <line x1="22" y1="3" x2="22" y2="41"/>
          <line x1="3" y1="22" x2="41" y2="22"/>
          <path d="M7 12 H37 M7 32 H37"/>
        </svg>
        <p class="contact-text" style="top:2px">www.hireavorlatrikebrenmoor.example</p>
      </div>

      <div class="contact-row row-phone">
        <svg width="44" height="40" viewBox="0 0 44 40" aria-hidden="true" stroke-width="2.6" stroke-linecap="round">
          <path d="M18 4 L12 6 C6 14 8 26 20 34 L26 36 L30 30 L24 25 L20 28 C15 24 14 18 15 13 L20 11 Z"/>
        </svg>
        <p class="contact-text" style="top:2px">(555) 014-2937</p>
      </div>
    </div>
  </section>
</body>
</html>
```